Crestfield Row sign

24"x36" sign for new home construction job site. Located in affluent in-town neighborhood in Midwest. Traditional american style homes. 2nd generation construction company. Sign needs to convey strength and elegance but not overly elaborate. Competition most has signs consisting of text.

Sign text reads:
Crestfield Row Builders
Custom Luxury for Over 20 years
248-391-0827

Target Market(s)

Upper middle income home buyers

Industry/Entity Type

Construction

Font styles to use
Serif
Decorative

Requirements
Must have
• Logo image no more than 2 colors
Nice to have
• Should be visible and legible from distance of 30'
Should not have
• Not just image of house as logo

```html
<!DOCTYPE html>
<html lang="en">
<head>
<meta charset="utf-8">
<title>Crestfield Row Builders – Job Site Sign</title>
<link href="https://fonts.googleapis.com/css2?family=Tinos:wght@400;700&family=Arimo:wght@700&display=swap" rel="stylesheet">
<style>
  :root {
    --backdrop: #e9ecef;
    --sign-white: #ffffff;
    --sign-edge: #c9ced4;
    --brand-blue: #1d5bb0;
    --band-blue: #1b55a6;
    --trade-black: #141414;
    --ink-white: #ffffff;
    --shadow-black: #0b0b0b;
  }
  * { margin: 0; padding: 0; box-sizing: border-box; }
  html, body {
    width: 1200px;
    height: 798px;
    overflow: hidden;
    background: var(--backdrop);
  }
  .canvas {
    width: 1200px;
    height: 798px;
    display: flex;
    align-items: center;
    justify-content: center;
  }
  .sign-panel {
    width: 640px;
    height: 560px;
    background: var(--sign-white);
    border: 3px solid var(--sign-edge);
    display: flex;
    flex-direction: column;
    box-shadow: 0 10px 30px rgba(0,0,0,0.12);
  }
  .brand-area {
    flex: 1;
    display: flex;
    flex-direction: column;
    align-items: center;
    justify-content: center;
    padding-top: 10px;
  }
  .brand-mark {
    width: 110px;
    height: 110px;
    background: var(--brand-blue);
    margin-bottom: 16px;
  }
  .brand-name {
    font-family: "Arimo", Arial, sans-serif;
    font-weight: 700;
    font-size: 44px;
    color: var(--brand-blue);
    line-height: 1;
    text-align: center;
  }
  .trade-line {
    font-family: "Tinos", "Times New Roman", serif;
    font-weight: 700;
    font-size: 76px;
    letter-spacing: 1px;
    text-transform: uppercase;
    color: var(--trade-black);
    line-height: 1;
    margin-top: 4px;
  }
  .info-band {
    background: var(--band-blue);
    height: 190px;
    display: flex;
    flex-direction: column;
    align-items: center;
    justify-content: center;
    gap: 10px;
  }
  .tagline {
    font-family: "Tinos", "Times New Roman", serif;
    font-weight: 400;
    font-size: 38px;
    color: var(--ink-white);
  }
  .phone {
    font-family: "Arimo", Arial, sans-serif;
    font-weight: 700;
    font-size: 66px;
    letter-spacing: 3px;
    color: var(--ink-white);
    text-shadow: 4px 4px 0 var(--shadow-black);
  }
</style>
</head>
<body>
  <main class="canvas">
    <section class="sign-panel">
      <div class="brand-area">
        <div class="brand-mark" role="img" aria-label="Company mark"></div>
        <h1 class="brand-name">Crestfield Row</h1>
        <p class="trade-line">Builders</p>
      </div>
      <div class="info-band">
        <p class="tagline">Custom Luxury for Over 20 years</p>
        <p class="phone">(248) 391-0827</p>
      </div>
    </section>
  </main>
</body>
</html>
```